Staffing Firm - Business Cards and Stationary
Business Cards, Letterhead, Envelopes and Brochure Layout
I need double sided standard sized Business Card [3.5" x 2"]
Use whatever fonts that you think are best.
Professional
Todd Dunlap
President/CEO
2250 North Birch Avenue, Ste 730
Houston, TX 77027
Direct Line - 832-555-0143
tdunlap@kelvor.com
www.kelvor.com
We would like them to be memorable but professional.
Possibly put the various divisions?
We will need layouts for each group/division.

```html
<!DOCTYPE html>
<html lang="en">
<head>
<meta charset="utf-8">
<title>Kelvor Staffing – Stationery Set</title>
<link rel="stylesheet" href="https://fonts.googleapis.com/css2?family=Cinzel:wght@400&family=Lato:wght@400;700&display=swap">
<style>
:root{
  --backdrop:#d9d9d6;
  --paper:#ffffff;
  --card-dark:#111111;
  --ink:#2a2a2a;
  --ink-soft:#6b6b6b;
  --rule:#9a9a9a;
  --div-solutions:#7a7a7a;
  --div-credit:#4f8a3a;
  --div-search:#7b3f8c;
  --div-services:#b5252a;
  --div-tech:#2c5f9e;
  --div-support:#d07a1e;
}
*{margin:0;padding:0;box-sizing:border-box}
html,body{width:1200px;height:874px;overflow:hidden}
body{background:var(--backdrop);position:relative;font-family:"Lato",Arial,sans-serif;color:var(--ink)}

/* wordmark */
.wordmark{font-family:"Cinzel",Georgia,serif;font-weight:400;color:var(--ink);display:flex;align-items:center;gap:4px;line-height:1.05;letter-spacing:.03em;white-space:nowrap}
.wordmark .dot{width:6px;height:6px;border-radius:50%;background:currentColor;flex:none}
.wordmark.on-dark{color:#fff}

/* business cards */
.card{position:absolute;width:134px;height:77px;box-shadow:0 1px 3px rgba(0,0,0,.25);overflow:hidden}
.card-front{left:34px;background:var(--paper)}
.card-back{left:178px;background:var(--card-dark)}
.card-front .wordmark{position:absolute;left:8px;top:8px;font-size:9px}
.card-front .division{position:absolute;left:40px;top:21px;font-size:4.4px;font-weight:700;letter-spacing:.02em;white-space:nowrap}
.card-front .person{position:absolute;left:8px;top:46px;width:56px}
.person .name{font-family:"Cinzel",Georgia,serif;font-size:6.2px;color:var(--ink);white-space:nowrap;letter-spacing:0}
.person .role{font-size:4.4px;color:var(--ink-soft);margin-top:2px;white-space:nowrap}
.card-front .divider{position:absolute;left:70px;top:32px;width:1px;height:38px;background:var(--rule)}
.card-front .contact{position:absolute;left:74px;top:33px;font-size:3.6px;line-height:1.45;color:var(--ink-soft);white-space:nowrap}
.card-back .wordmark{position:absolute;left:8px;top:10px;font-size:9px}
.card-back .tagline{position:absolute;left:8px;right:8px;bottom:9px;font-size:3.6px;color:#cfcfcf;letter-spacing:.03em;white-space:nowrap}
.card-back .tagline b{font-weight:700}

/* letterhead */
.letterhead{position:absolute;left:379px;top:247px;width:334px;height:440px;background:var(--paper);box-shadow:0 2px 5px rgba(0,0,0,.25)}
.letterhead .wordmark{position:absolute;left:22px;top:24px;font-size:15px}
.letterhead .division{position:absolute;left:84px;top:48px;font-size:6px;font-weight:700;color:var(--div-tech)}
.letterhead .address{position:absolute;left:206px;top:26px;font-size:4.6px;line-height:1.5;color:var(--ink-soft)}

/* divisions footer */
.division-list{display:flex;gap:10px;font-size:4.4px;font-weight:700;white-space:nowrap}
.letterhead .division-list{position:absolute;left:18px;bottom:18px}
.c-solutions{color:var(--div-solutions)}
.c-credit{color:var(--div-credit)}
.c-search{color:var(--div-search)}
.c-services{color:var(--div-services)}
.c-tech{color:var(--div-tech)}
.c-support{color:var(--div-support)}

/* envelopes */
.envelope{position:absolute;left:790px;width:360px;height:176px;background:var(--paper);box-shadow:0 2px 5px rgba(0,0,0,.25)}
.envelope-front{top:242px}
.envelope-front .wordmark{position:absolute;left:14px;top:14px;font-size:12px}
.envelope-front .division{position:absolute;left:64px;top:33px;font-size:5px;font-weight:700;color:var(--div-tech)}
.envelope-front .address{position:absolute;left:14px;top:44px;font-size:4.4px;line-height:1.5;color:var(--ink-soft)}
.envelope-back{top:449px}
.envelope-back svg{position:absolute;inset:0}
.envelope-back .wordmark{position:absolute;left:0;right:0;top:66px;justify-content:center;font-size:11px}
.envelope-back .division-list{position:absolute;left:14px;bottom:12px;gap:12px;font-size:4.6px}
</style>
</head>
<body>

<!-- business card fronts -->
<section class="card card-front" style="top:108px">
  <div class="wordmark"><span class="dot"></span>Kelvor Staffing</div>
  <div class="division c-solutions">staffing solutions</div>
  <div class="person"><div class="name">Todd Dunlap</div><div class="role">President/CEO</div></div>
  <div class="divider"></div>
  <div class="contact">2250 North Birch Avenue, Ste 730<br>Houston, TX 77027<br>Direct Line - 832-555-0143<br>tdunlap@kelvor.com<br>www.kelvor.com</div>
</section>
<section class="card card-front" style="top:209px">
  <div class="wordmark"><span class="dot"></span>Kelvor Staffing</div>
  <div class="division c-credit">credit and risk group</div>
  <div class="person"><div class="name">Todd Dunlap</div><div class="role">President/CEO</div></div>
  <div class="divider"></div>
  <div class="contact">2250 North Birch Avenue, Ste 730<br>Houston, TX 77027<br>Direct Line - 832-555-0143<br>tdunlap@kelvor.com<br>www.kelvor.com</div>
</section>
<section class="card card-front" style="top:307px">
  <div class="wordmark"><span class="dot"></span>Kelvor Staffing</div>
  <div class="division c-search">professional search group</div>
  <div class="person"><div class="name">Todd Dunlap</div><div class="role">President/CEO</div></div>
  <div class="divider"></div>
  <div class="contact">2250 North Birch Avenue, Ste 730<br>Houston, TX 77027<br>Direct Line - 832-555-0143<br>tdunlap@kelvor.com<br>www.kelvor.com</div>
</section>
<section class="card card-front" style="top:408px">
  <div class="wordmark"><span class="dot"></span>Kelvor Staffing</div>
  <div class="division c-services">staffing services group</div>
  <div class="person"><div class="name">Todd Dunlap</div><div class="role">President/CEO</div></div>
  <div class="divider"></div>
  <div class="contact">2250 North Birch Avenue, Ste 730<br>Houston, TX 77027<br>Direct Line - 832-555-0143<br>tdunlap@kelvor.com<br>www.kelvor.com</div>
</section>
<section class="card card-front" style="top:509px">
  <div class="wordmark"><span class="dot"></span>Kelvor Staffing</div>
  <div class="division c-tech">technology services group</div>
  <div class="person"><div class="name">Todd Dunlap</div><div class="role">President/CEO</div></div>
  <div class="divider"></div>
  <div class="contact">2250 North Birch Avenue, Ste 730<br>Houston, TX 77027<br>Direct Line - 832-555-0143<br>tdunlap@kelvor.com<br>www.kelvor.com</div>
</section>

<!-- business card backs -->
<section class="card card-back" style="top:108px">
  <div class="wordmark on-dark"><span class="dot"></span>Kelvor Staffing</div>
  <div class="tagline">people who fit your business · <b class="c-solutions">staffing solutions</b></div>
</section>
<section class="card card-back" style="top:209px">
  <div class="wordmark on-dark"><span class="dot"></span>Kelvor Staffing</div>
  <div class="tagline">people who fit your business · <b class="c-credit">credit and risk group</b></div>
</section>
<section class="card card-back" style="top:307px">
  <div class="wordmark on-dark"><span class="dot"></span>Kelvor Staffing</div>
  <div class="tagline">people who fit your business · <b class="c-search">professional search group</b></div>
</section>
<section class="card card-back" style="top:408px">
  <div class="wordmark on-dark"><span class="dot"></span>Kelvor Staffing</div>
  <div class="tagline">people who fit your business · <b class="c-services">staffing services group</b></div>
</section>
<section class="card card-back" style="top:509px">
  <div class="wordmark on-dark"><span class="dot"></span>Kelvor Staffing</div>
  <div class="tagline">people who fit your business · <b class="c-tech">technology services group</b></div>
</section>

<!-- letterhead -->
<section class="letterhead">
  <div class="wordmark"><span class="dot"></span>Kelvor Staffing</div>
  <div class="division">staffing solutions</div>
  <div class="address">2250 North Birch Avenue, Ste 730<br>Houston, TX 77027<br>832-555-0143<br>www.kelvor.com</div>
  <div class="division-list">
    <span class="c-credit">credit and risk group</span>
    <span class="c-search">professional search group</span>
    <span class="c-services">staffing services group</span>
    <span class="c-tech">technology services group</span>
  </div>
</section>

<!-- envelope front -->
<section class="envelope envelope-front">
  <div class="wordmark"><span class="dot"></span>Kelvor Staffing</div>
  <div class="division">staffing solutions</div>
  <div class="address">2250 North Birch Avenue, Ste 730<br>Houston, TX 77027</div>
</section>

<!-- envelope back -->
<section class="envelope envelope-back">
  <svg width="360" height="176" viewBox="0 0 360 176" aria-hidden="true">
    <polyline points="0,4 180,92 360,4" fill="none" stroke="#c9c9c9" stroke-width="1"/>
    <polyline points="0,176 150,84" fill="none" stroke="#e2e2e2" stroke-width="1"/>
    <polyline points="360,176 210,84" fill="none" stroke="#e2e2e2" stroke-width="1"/>
  </svg>
  <div class="wordmark"><span class="dot"></span>Kelvor Staffing</div>
  <div class="division-list">
    <span class="c-credit">credit and risk group</span>
    <span class="c-search">professional search group</span>
    <span class="c-services">staffing services group</span>
    <span class="c-tech">technology services group</span>
    <span class="c-support">staffing services group</span>
  </div>
</section>

</body>
</html>
```